Website Redesign Project

Bright Harbor Planning provides project management and project controls consultancy services to companies in many industry sectors, within Australia and overseas. My company has been developing a business brand through forging strong business relationships within industry. We provide innovative tools, concepts and solutions to management teams to assist them in better plan and managing there project portfolios.
SECTORS OF INDUSTRY WE SERVICE
★Oil & Gas
★Minerals & Metals
★Petrochemical
★Manufacturing
★Building & Construction
★Telecommunications
★Rail
★Civil
OLD WEBSITE
My old website www.brightharborplanning.com.au needs a complete overhaul in terms of how the web pages look and feel. I am trying to get away from the grey, washed out look as it is uninviting and dull. My clients commented that my webpage does not reflect who I am as a company or my core values. Think total redesign
DESIGN
I would like a webpage design that is modern and has a corporate image. It must be elegant, classy, and have an overall glossy appearance. I want something exciting that creates some excellent feedback from clients. It needs to have a savvy appearance and an attitude of a market leader. A generic website template cannot be used as I provide a unique service to clients. I do not need a website design that looks like my compeditors, I want something that stands out in the crowd and effectivly markets my bussinesses brand. I want my website to represent quality, so only high resolution images that are clear, sharp and in focus can be used. With this design, throw your standard webpage design concepts out the window, as I want something fresh, innovative, exciting and inviting. The overall design should appear uncluttered as all content needs to be there for a reason, so think functional.
It must be professional and of the highest calibre as my clients expect nothing less. I provide clients with innovative tools, concepts and solutions, so the design needs to be edgy and creative to align with my company’s core business services. The new design must promote the company’s brand and us as a market leader. It must communicate that we service many industry sectors and reflect our company’s creativity, vision, energy and drive.
WEBPAGE WRITTEN CONTENT
I am happy with the written content on each page within my old website. You may arrange the text how you see fit within the new design. On the main page of my old website the text is under scored, I am not a big fan of this. I currently do not like the format the text is in, I am looking for a formatt that is easy to read, looks flattering and pleasing to the eye.
MAIN PAGE DESIGN
The main page design needs to focus on my company as a brand, it must promote that I service many industry sectors. My old webpage had me pigeon holed as only providing services to oil and gas. This is incorrect as I service oil & gas, metals and minerals, Petrochemical, Manufacturing, Building & Construction, Telecommunications, Rail and civil.
WEBPAGE COLUR PREFERENCE
Prefer a white background with plenty of colour
TESTIMONIAL TAB
The testimonial tab on the task bar can be removed as it is no longer required.
FINISHED PRODUCT
The finished product will be uploaded by you to a nominated web hosting account. I will need a copy of all files associated with the design. A copy of the finished product will also be provided in formats that can me imported to Xara Pro Designer as I will update my website in 6 months or so using this tool.
Updates
I have updated the design brief after recieving feedback from several designers
Thanks
Reason: Some designers have asked for more time
Hi All
I have just launched another project called "bright harbor planning business card redesign project", you are all welcome to join this project.
Thanks
Target Market(s)
★Oil and Gas
★Mining and Resources
★Building and infrastructure
★Petrochemical
★Civil and roads
★Rail
Industry/Entity Type
Industry
Requirements
Must have
- ★Draw you in
★Hold your attention
★Identify company brand
★Highlight skills experience and expertise
★Be a unique design not generic
Should not have
- ★The webpage design should not be old fashioned
★ The design should not be based off a generic design template
★The webpage should not be cluttered; everything needs to be there for a reason.

```html
<!DOCTYPE html>
<html lang="en">
<head>
<meta charset="utf-8">
<title>Bright Harbor Planning – Home</title>
<link href="https://fonts.googleapis.com/css2?family=Arimo:wght@400;700&family=Tinos&display=swap" rel="stylesheet">
<style>
:root{
  --red:#e31b23;
  --red-dark:#c4141b;
  --ink:#222;
  --text:#444;
  --muted:#666;
  --rule:#bdbdbd;
  --header-top:#f7f7f7;
  --header-bottom:#e4e4e4;
  --footer:#3b3b3b;
  --footer-text:#b8b8b8;
  --sea-light:#3f6f9c;
  --sea-dark:#234a73;
}
*{margin:0;padding:0;box-sizing:border-box}
html,body{width:1196px;height:1200px;overflow:hidden;background:#fff}
body{position:relative;font-family:"Arimo",Arial,sans-serif;color:var(--text)}
.abs{position:absolute}

.site-header{position:absolute;left:0;top:0;width:1196px;height:171px;
  background:linear-gradient(var(--header-top),var(--header-bottom));}
.brand{left:188px;top:42px;display:flex;align-items:center;gap:10px}
.brand-mark{width:30px;height:30px;background:var(--red)}
.brand-name{font-size:26px;font-weight:700;color:var(--ink);letter-spacing:-.3px}
.brand-tagline{left:228px;top:83px;font-size:9px;color:#333}

.contact{right:202px;font-size:15px;color:#222;display:flex;align-items:center;gap:8px}
.contact-phone{top:46px}
.contact-email{top:73px}

.main-nav{left:0;top:138px;height:33px;width:1196px}
.nav-item{position:absolute;top:9px;font-size:13px;color:#222}
.nav-item.is-active{top:0;left:194px;width:73px;height:33px;background:var(--red);color:#fff;text-align:center;line-height:33px}
.nav-item.is-active::after{content:"";position:absolute;left:32px;bottom:-7px;border:5px solid transparent;border-top:7px solid var(--red);border-bottom:0}

.hero{left:188px;top:199px;width:820px;height:356px;background:#fff;border:1px solid #ddd;padding:6px;box-shadow:0 12px 14px -10px rgba(0,0,0,.35)}
.hero-photo{width:100%;height:100%;background:linear-gradient(180deg,var(--sea-dark) 0%,var(--sea-light) 55%,#7c8a8c 80%,#5e6a6b 100%)}

.welcome-title{left:0;width:1196px;top:586px;text-align:center;font-family:"Tinos",Georgia,serif;font-size:24px;color:var(--ink);font-weight:400}
.welcome-title .cap{color:var(--red)}
.welcome-text{left:196px;width:805px;top:631px;text-align:center;font-size:12px;line-height:17px;color:var(--text)}
.btn-primary{left:541px;top:711px;width:113px;height:35px;background:var(--red);color:#fff;font-size:14px;text-align:center;line-height:35px}

.divider{left:188px;top:772px;width:820px;height:1px}
.divider::before,.divider::after{content:"";position:absolute;top:0;height:1px;background:var(--rule);width:388px}
.divider::before{left:0}.divider::after{right:0}
.divider-ornament{position:absolute;left:391px;top:-6px;width:38px;height:12px;border-radius:6px;background:var(--red)}

.feature{top:792px;width:260px}
.feature-title{font-family:"Tinos",Georgia,serif;font-size:22px;font-weight:400;color:var(--ink)}
.feature-title .accent{color:var(--red)}
.feature-sub{font-size:11px;color:var(--muted);margin-top:1px;letter-spacing:.1px}
.feature-list{list-style:none;margin-top:17px}
.feature-list li{font-size:11px;color:var(--text);height:21.35px;padding-left:13px;position:relative}
.feature-list li::before{content:"";position:absolute;left:1px;top:3px;width:5px;height:5px;border-right:2px solid var(--red);border-top:2px solid var(--red);transform:rotate(45deg)}
.btn-more{position:absolute;top:225px;left:-1px}

.site-footer{position:absolute;left:0;top:1080px;width:1196px;height:120px;background:var(--footer)}
.footer-nav{left:190px;top:26px;font-size:12px;color:var(--footer-text)}
.footer-nav span{padding:0 5px;color:#888}
.copyright{left:190px;top:48px;font-size:11px;color:var(--footer-text)}
.social{left:905px;top:18px;display:flex;gap:4px}
.social i{display:block;width:23px;height:22px;background:linear-gradient(#555,#1e1e1e)}
</style>
</head>
<body>

<header class="site-header">
  <div class="abs brand">
    <span class="brand-mark"></span>
    <span class="brand-name">Bright Harbor Planning</span>
  </div>
  <div class="abs brand-tagline">Providing Effective Project Controls and Management Solutions</div>

  <div class="abs contact contact-phone">
    <svg width="26" height="16" viewBox="0 0 26 16"><path d="M2 6c0-4 22-4 22 0l-1 3h-5l-1-3H9L8 9H3z" fill="#111"/><rect x="6" y="8" width="14" height="8" rx="2" fill="#111"/><circle cx="13" cy="12" r="2.5" fill="#eee"/></svg>
    <span>61 0400 555 019</span>
  </div>
  <div class="abs contact contact-email">
    <svg width="24" height="15" viewBox="0 0 24 15"><rect width="24" height="15" fill="#111"/><path d="M1 1l11 8 11-8" stroke="#eee" stroke-width="1.4" fill="none"/></svg>
    <span>alexreed@brightharborplanning.com.au</span>
  </div>

  <nav class="abs main-nav">
    <span class="nav-item is-active">Home</span>
    <span class="nav-item" style="left:284px">About Us</span>
    <span class="nav-item" style="left:372px">Expertise</span>
    <span class="nav-item" style="left:461px">Knowledge</span>
    <span class="nav-item" style="left:560px">Experience</span>
    <span class="nav-item" style="left:660px">Projects</span>
    <span class="nav-item" style="left:742px">Focus</span>
    <span class="nav-item" style="left:812px">Recruitment</span>
    <span class="nav-item" style="left:917px">Contact Us</span>
  </nav>
</header>

<section class="abs hero">
  <div class="hero-photo" role="img" aria-label="Aerial photograph of an offshore oil and gas platform on a blue sea with a flare tower"></div>
</section>

<h1 class="abs welcome-title"><span class="cap">W</span>elcome to <span class="cap">B</span>right <span class="cap">H</span>arbor <span class="cap">P</span>lanning</h1>
<p class="abs welcome-text">I provide services to companies in the mining and oil and gas sector to enabling them to plan and manage their construction projects more effectively. This is achieved by evaluating the businesses practices and them implementing different tools and solutions. My clients are then able to plan and deliver their projects, on time and within their budgets. I am able to provide services to both large and small scale businesses within Australian and Overseas. I offer my clients value by providing, exceptional skills and expertise at a competitive market rate.</p>
<a class="abs btn-primary">Read More</a>

<div class="abs divider"><span class="divider-ornament" role="img" aria-label="Decorative red scroll ornament"></span></div>

<section class="abs feature" style="left:188px">
  <h2 class="feature-title"><span class="accent">We</span> Expertise</h2>
  <p class="feature-sub">DEVELOP, DESIGN &amp; IMPLEMENT</p>
  <ul class="feature-list">
    <li>Project Management</li><li>Project Control</li><li>Process Maping Approval</li><li>Solid Foundations</li><li>Resources</li><li>Assisting Clients</li><li>System Design &amp; Implementation</li>
  </ul>
  <svg class="btn-more" width="116" height="28" viewBox="0 0 116 28"><path d="M0 0h104l11 14-11 14H0z" fill="var(--red)"/><text x="11" y="19" font-family="Arimo,Arial,sans-serif" font-size="13" fill="#fff">Read More</text><path d="M93 8v12M87 14h12" stroke="#fff" stroke-width="3"/></svg>
</section>

<section class="abs feature" style="left:470px">
  <h2 class="feature-title">Our <span class="accent">Projects</span></h2>
  <p class="feature-sub">ASSOCIATED &amp; ASSISTING</p>
  <ul class="feature-list">
    <li>Oil &amp; Gas</li><li>Iron Ore</li><li>Coal</li><li>Petrochemical</li><li>Civil</li><li>Engineering</li><li>manufacuring</li>
  </ul>
  <svg class="btn-more" width="116" height="28" viewBox="0 0 116 28"><path d="M0 0h104l11 14-11 14H0z" fill="var(--red)"/><text x="11" y="19" font-family="Arimo,Arial,sans-serif" font-size="13" fill="#fff">Read More</text><path d="M93 8v12M87 14h12" stroke="#fff" stroke-width="3"/></svg>
</section>

<section class="abs feature" style="left:751px">
  <h2 class="feature-title"><span class="accent">We</span> Focussing</h2>
  <p class="feature-sub">ASSOCIATED &amp; ASSISTING</p>
  <ul class="feature-list">
    <li>Providing Direction</li><li>Vision for the Future</li><li>Removing Business Risks</li><li>Analysis</li><li>Planning</li><li>Setting Achievable Timelines</li><li>Experience</li>
  </ul>
  <svg class="btn-more" width="116" height="28" viewBox="0 0 116 28"><path d="M0 0h104l11 14-11 14H0z" fill="var(--red)"/><text x="11" y="19" font-family="Arimo,Arial,sans-serif" font-size="13" fill="#fff">Read More</text><path d="M93 8v12M87 14h12" stroke="#fff" stroke-width="3"/></svg>
</section>

<footer class="site-footer">
  <div class="abs footer-nav">Home<span>|</span>About Us<span>|</span>Expertise<span>|</span>Knowledge<span>|</span>Experience<span>|</span>Projects<span>|</span>Focus<span>|</span>Recruitment<span>|</span>Contact Us</div>
  <div class="abs copyright">2013 Bright Harbor Planning. All Rights Reserved</div>
  <div class="abs social" aria-label="Social links"><i></i><i></i><i></i><i></i></div>
</footer>

</body>
</html>
```